Web Design & Programming for Health & Wellness Coaching Company (PageFoundry or Scribeloom)

Business Info: I'm starting a health coaching business (Colette Marsh, PhD, Health & Wellness Coaching @ colettemarshwell.com) and need some help designing my website (colettemarshwell.com).

Basics: I have the domain purchased on pagefoundry.com that is also linked to Scribeloom (so designer/programmer can program into pagefoundry.com or Scribeloom.com). I want my primary color to be aqua blue (see 1st photo/pdf attached) and my secondary colors to be spring green (1) and deep purple/magenta (see 2nd photo/pdf attached as well as the last photo attached).

There will be 5 pages: 1) Home; 2) Services; 3) Coaching Philosophy; 4) About Me; 5) Blog; 6) Client Resources; 7) Contact Me

I want there to be a banner at the top of each page, on the right-hand side (align right) that has links to all other pages, as well as a “book a consult” icon (that links to an appointment book where clients can see my schedule and book an appointment) and a cart icon, where clients can check out and pay. The cart will need to be linked to a pay service. The banner should roughly appear as follows:
Home | Services | Coaching Philosophy | About Me | [Book a Consult Icon] | [Cart Icon]

I also want there to be a small, centered area for hyperlinks at the bottom of each page that appears as follows (with everything hyperlinked):

Home | Services | Coaching Philosophy | About Me
555-314-2786 | colette@colettemarshwell.com
Colette Marsh, PhD, LLC | © 2022

“Home Page:” I would like my home page to have 3-4 main aspects: 1) a marquis of photos of me (included below; one main photo, but with options for clients to right/left click to scroll through several photos); 2-3) space for text about my coaching philosophy and program 3) a marquis of client testimonials that clients can scroll through. I like the setup of this homepage: https://www.tidewellcoach.example but using my color scheme (below). I want the home page to have the water background shown in the first image (but not the surfers).

“Services page:” I offer the following 5 services: 1) Free Health History Consultation; 2) Standard 6-Month Program; 3) Deluxe 6-Month Program; 4) Coastal Calm Insight Card Reading; 5) Customized Options.

I want each service to be shown on the Services page and to contain a “Book Appointment” or “Purchase” button/link (Services #1-2 should have the “Book appointment” button and services #3-5 should have the “Purchase” button). I want the “Book appointment” button to link to a calendar where clients can see my schedule and book an appointment. Both links should also cause the item to appear in the cart, and the cart should be linked to a pay feature that can take clients’ credit card info, etc.

The “About Me” Page should say “About Me” then have 1 photo (with arrow options on both sides so clients can scroll through different photos). Below the photo should be a block of text where I can include a few paragraphs about me. Below the text should be links to the following pages, which can appear as follows:

Find Me on Social Media:
Current: https://olvera-institute.example/profile/cmarsh
ConnectWork: https://www.connectworknet.example/in/colette-marsh-52718406/
FriendSpace: https://www.friendspace.example/colette.marsh
SnapGallery: https://www.snapgallery.example/colettem_hikes/?hl=en

The “Coaching Philosophy” page should be similar to the “About Me” page (minus the “Follow Me on social media” part). This page should have 2 icon/links below the text: 1 that says “Let’s Get Started” and directs patients to my calendar where they can book a free 1hr health coaching consultation; 1 that says “Book a Service” and takes clients to the services page.

The “Blog” page will be a standard blog page.

The “Client Resources” page will be for client resources. I would like for this page to require clients to enter their a login name and password (provided by me).

More about my business:
My health coaching certification is through the Academy of Holistic Dietetics (AHD, holisticdieteticsacademy.com). I also have a PhD in Basic Biomedical Science & Neuroscience (specializing in addiction) and post-doctorate experience at the Olvera Institute of Botanical Healing in alternative/complementary and integrative health interventions for binge eating and obesity (things like 12-step interventions, yoga, acupuncture, meditation, herbs, etc.).

My health coaching practice centers around 2 concepts: 1) the client can heal his/herself by him/herself; I am simply here to help the client tap into his/her own healing intuition; 2) I believe in wholistic healing that brings primary and secondary foods into balance. Secondary foods are the foods we put on our plate and eat. Primary foods are everything else in our life that nourishes us (e.g., creativity, relationships, movement, joy, finances, etc.). When the secondary foods are a problem, it's usually a sign that our primary foods are imbalanced, so I help clients identify how to rebalance both.

I also included some sample photos that will on the "about me" page of my website. I focus on connection, movement, and nature, so lots of nature themes. Mountains.

Here are some other relevant "about me" websites:

Target Market(s)

Adult females and males who live busy lives and want help and support in creating transformation and breakthroughs, on their plates (nutrition) and in their lives.

Industry/Entity Type

Health and Wellness

Number of Pages Required

5+ page

Font styles to use
Serif
Sans Serif

Colors
0094D4
00A9DD
6FCCEA
C7EBF8
E9F6FB

Requirements
Must have
• See project description
Nice to have
• See project description

```html
<!DOCTYPE html>
<html lang="en">
<head>
<meta charset="utf-8">
<title>Colette Marsh, PhD — Health &amp; Wellness Coaching</title>
<link href="https://fonts.googleapis.com/css2?family=Poppins:wght@400;500;600;700&family=Open+Sans:wght@400;600&display=swap" rel="stylesheet">
<style>
:root{
  --ocean-deep:#0b3550;
  --ocean-mid:#14607f;
  --aqua:#22f3f8;
  --aqua-dark:#12d6e0;
  --green:#2ded5c;
  --blue:#2a9cd6;
  --ink:#1b1b1b;
  --text:#3c3c3c;
  --muted:#6b6b6b;
  --link:#17c6e6;
  --footer:#0d1a29;
  --white:#fff;
}
*{margin:0;padding:0;box-sizing:border-box}
html,body{width:1200px;height:4471px;overflow:hidden;background:var(--white)}
body{position:relative;font-family:"Open Sans",sans-serif;color:var(--text)}
.abs{position:absolute}
.heading{font-family:"Poppins",sans-serif;color:var(--ink);font-weight:500}
.center{text-align:center}
.btn{position:absolute;display:flex;align-items:center;justify-content:center;gap:6px;font-family:"Poppins",sans-serif;font-weight:500;color:var(--white);background:var(--green);border-radius:3px;font-size:15px;text-decoration:none}
.photo{position:absolute;border-radius:6px}
.section-rule{position:absolute;left:575px;width:50px;height:2px;background:var(--link)}

/* hero */
.hero{position:absolute;left:0;top:0;width:1200px;height:557px;background:radial-gradient(ellipse at 30% 40%,#1b6b8c 0%,var(--ocean-mid) 35%,var(--ocean-deep) 100%)}
.logo{position:absolute;font-family:"Poppins",sans-serif;font-weight:600;color:var(--white);font-size:34px;letter-spacing:.5px}
.main-nav{position:absolute;left:400px;top:34px;display:flex;gap:28px;font-family:"Poppins",sans-serif;font-size:14px;color:var(--white)}
.hero-photo{position:absolute;left:695px;top:146px;width:394px;height:411px;border:8px solid var(--green);border-bottom:none;border-radius:14px 14px 0 0;background:linear-gradient(160deg,#a7c8e0 0%,#5f8f3b 45%,#3f7a2a 100%)}
.dots{position:absolute;left:568px;top:514px;display:flex;gap:5px}
.dots span{width:11px;height:11px;border:1.5px solid var(--white);border-radius:50%}
.dots span.on{background:var(--blue)}

/* services */
.service{position:absolute;top:726px;width:238px;height:382px;text-align:center;color:var(--white)}
.service.blue{background:var(--blue)} .service.green{background:var(--green)}
.service .icon{position:absolute;left:67px;top:30px;width:104px;height:104px;border-radius:50%;background:rgba(255,255,255,.35);display:flex;align-items:center;justify-content:center}
.service .icon i{width:84px;height:84px;border-radius:50%;background:var(--white);display:flex;align-items:center;justify-content:center}
.service h3{position:absolute;top:154px;left:10px;right:10px;font-family:"Poppins",sans-serif;font-weight:600;font-size:17px;line-height:26px}
.service p{position:absolute;top:216px;left:22px;right:22px;font-size:14px;line-height:26px;opacity:.9}
.service .book{position:absolute;left:25px;top:302px;width:188px;height:42px;border:1.5px solid var(--white);border-radius:3px;display:flex;align-items:center;justify-content:center;gap:6px;font-family:"Poppins",sans-serif;font-weight:500;font-size:15px}
.round-arrow{position:absolute;width:48px;height:48px;border-radius:50%;display:flex;align-items:center;justify-content:center}

/* bands */
.band{position:absolute;left:0;width:1200px;background:linear-gradient(180deg,var(--aqua) 0%,#1de8f2 60%,var(--aqua-dark) 100%)}
.chev{position:absolute}
.band-text{position:absolute;left:130px;width:940px;text-align:center;font-size:14.5px;line-height:26px;color:#23393f}
.social-ring{position:absolute;width:38px;height:38px;border:1.5px solid var(--ink);border-radius:50%}

/* blog */
.blog-meta{font-size:12px;color:var(--muted);display:flex;align-items:center;gap:6px}
.blog-title{font-family:"Poppins",sans-serif;font-weight:500;font-size:16px;color:var(--ink);line-height:25px}
.blog-ex{font-size:12px;line-height:19px;color:#444}
.read{font-family:"Poppins",sans-serif;font-weight:600;font-size:14px;color:var(--link)}

/* practice */
.practice{position:absolute;top:3801px;width:160px;text-align:center}
.practice .ring{margin:0 auto;width:108px;height:108px;border-radius:50%;background:#c9f7d6;display:flex;align-items:center;justify-content:center}
.practice .ring i{width:88px;height:88px;border-radius:50%;background:var(--green);border:4px solid var(--white);display:flex;align-items:center;justify-content:center}
.practice span{display:block;margin-top:30px;font-family:"Poppins",sans-serif;font-weight:500;font-size:21px;color:var(--ink)}

/* footer */
.footer{position:absolute;left:0;top:4043px;width:1200px;height:428px;background:var(--footer);color:var(--white)}
.footer h4{position:absolute;top:104px;font-family:"Poppins",sans-serif;font-weight:600;font-size:17px}
.footer ul{position:absolute;list-style:none;font-family:"Poppins",sans-serif;font-weight:500;font-size:14px;line-height:26px}
.contact-row{position:absolute;left:571px;display:flex;gap:12px;font-size:15px;line-height:24px}
.foot-social{position:absolute;top:4240px;width:40px;height:40px;border-radius:50%;background:var(--white)}
.pay{width:34px;height:20px;border-radius:3px}
</style>
</head>
<body>

<!-- Header / hero -->
<header class="hero">
  <div class="logo" style="left:110px;top:20px">colettemarsh</div>
  <nav class="main-nav">
    <span>Home</span><span>Services</span><span>Coaching Philosophy</span><span>About Me</span>
    <span style="display:flex;gap:12px;align-items:center">
      <svg width="16" height="14" viewBox="0 0 16 14"><path d="M1 1h3l2 8h8l1-6H5" fill="none" stroke="#fff" stroke-width="1.8"/><circle cx="7" cy="12" r="1.3" fill="#fff"/><circle cx="13" cy="12" r="1.3" fill="#fff"/></svg>
      |
      <svg width="14" height="14" viewBox="0 0 14 14"><circle cx="6" cy="6" r="4.5" fill="none" stroke="#fff" stroke-width="2"/><path d="M9.5 9.5 13 13" stroke="#fff" stroke-width="2"/></svg>
    </span>
  </nav>
  <a class="btn" style="left:927px;top:28px;width:160px;height:38px;font-size:14px">&#9638; Book a Consult</a>

  <p class="heading abs" style="left:110px;top:182px;font-size:38px;color:var(--white);font-weight:400">Welcome to</p>
  <h1 class="heading abs" style="left:108px;top:228px;font-size:66px;color:var(--white);font-weight:600">Colettemarsh</h1>
  <p class="abs" style="left:110px;top:318px;width:470px;font-size:15px;line-height:26px;color:var(--white)">Lorem ipsum dolor sit amet, consectetur adipiscing elit, sed do eiusmod tempor incididunt ut labore et dolore magna aliqua.</p>
  <a class="btn" style="left:110px;top:387px;width:213px;height:44px">&#9638; Book an Appointment</a>

  <div class="hero-photo" role="img" aria-label="Photo of the coach running on a grassy mountain trail beneath a chairlift"></div>
  <div class="dots"><span></span><span class="on"></span><span></span><span></span><span></span></div>
</header>

<!-- Services -->
<section>
  <h2 class="heading abs center" style="left:0;width:1200px;top:636px;font-size:31px">Our Services</h2>
  <div class="section-rule" style="top:677px"></div>

  <div class="round-arrow" style="left:44px;top:893px;background:var(--white);box-shadow:0 0 8px rgba(0,0,0,.18)">
    <svg width="12" height="16"><path d="M9 2 3 8l6 6" fill="none" stroke="var(--green)" stroke-width="2"/></svg>
  </div>
  <div class="round-arrow" style="left:1107px;top:893px;background:var(--green)">
    <svg width="12" height="16"><path d="m3 2 6 6-6 6" fill="none" stroke="#fff" stroke-width="2"/></svg>
  </div>

  <article class="service blue" style="left:111px">
    <div class="icon"><i><svg width="44" height="44" viewBox="0 0 44 44" fill="none" stroke="var(--blue)" stroke-width="2"><rect x="6" y="14" width="22" height="24"/><rect x="26" y="6" width="14" height="14"/><path d="M11 22h12M11 28h12M30 11h6M30 15h6M4 38h38"/></svg></i></div>
    <h3>Free Health History Consultation</h3>
    <p>Sed ut perspiciatis unde omnis iste natus error sit voluptatem accusantium</p>
    <div class="book">&#9638; Book Appointment</div>
  </article>
  <article class="service green" style="left:358px">
    <div class="icon"><i><svg width="44" height="44" viewBox="0 0 44 44" fill="none" stroke="var(--green)" stroke-width="2"><path d="M10 4h18l8 8v28H10z"/><path d="M15 16h14M15 22h14M15 28h8"/><circle cx="32" cy="34" r="6"/><path d="m29 34 2 2 4-4"/></svg></i></div>
    <h3>Standard 6-Month Program</h3>
    <p>Sed ut perspiciatis unde omnis iste natus error sit voluptatem accusantium</p>
    <div class="book">&#9638; Book Appointment</div>
  </article>
  <article class="service blue" style="left:604px">
    <div class="icon"><i><svg width="44" height="44" viewBox="0 0 44 44" fill="none" stroke="var(--blue)" stroke-width="2"><path d="M22 38S5 27 5 16a8.5 8.5 0 0 1 17-2 8.5 8.5 0 0 1 17 2c0 11-17 22-17 22z"/><path d="M22 16v12M16 22h12"/></svg></i></div>
    <h3>Coastal Calm Insight Card Reading</h3>
    <p>Sed ut perspiciatis unde omnis iste natus error sit voluptatem accusantium</p>
    <div class="book">&#9638; Book Appointment</div>
  </article>
  <article class="service green" style="left:851px">
    <div class="icon"><i><svg width="44" height="44" viewBox="0 0 44 44" fill="none" stroke="var(--green)" stroke-width="2"><rect x="6" y="6" width="32" height="32" rx="3"/><circle cx="22" cy="22" r="7"/><circle cx="22" cy="22" r="2.5"/><path d="M22 11v4M22 29v4M11 22h4M29 22h4"/></svg></i></div>
    <h3>Customized Options</h3>
    <p>Sed ut perspiciatis unde omnis iste natus error sit voluptatem accusantium</p>
    <div class="book">&#9638; Book Appointment</div>
  </article>
</section>

<!-- About -->
<section>
  <div class="band" style="top:1428px;height:705px"></div>
  <div class="photo" style="left:182px;top:1205px;width:836px;height:473px;background:linear-gradient(135deg,#5d6770 0%,#8c7f70 45%,#a99a88 70%,#6a7780 100%)" role="img" aria-label="Portrait photo of the coach smiling outdoors"></div>
  <svg class="chev" style="left:70px;top:1712px" width="20" height="34"><path d="M17 3 4 17l13 14" fill="none" stroke="#111" stroke-width="3.5"/></svg>
  <svg class="chev" style="left:1105px;top:1712px" width="20" height="34"><path d="m3 3 13 14L3 31" fill="none" stroke="#111" stroke-width="3.5"/></svg>
  <p class="heading abs center" style="left:0;width:1200px;top:1729px;font-size:17px">ABOUT ME</p>
  <h2 class="heading abs center" style="left:0;width:1200px;top:1758px;font-size:30px">Colette Marsh, PhD</h2>
  <p class="band-text" style="top:1811px">Dr. Marsh is a Post-doctoral Research Investigator in the Larchmont Research Institute. She is committed to producing interdisciplinary clinical research that explores psychological and biomedical outcomes associated with complementary and integrative health (CIH) treatment approaches to mental health problems (binge eating disorder) and underlying hormonal dysregulations.Dr. Marsh received her PhD in Biomedical Science and Neuroscience from the University of North Plains's Graduate School in conjunction with the Wexley School of Medicine in 2018.</p>
  <a class="btn" style="left:535px;top:1971px;width:128px;height:40px">Read More</a>
  <div class="social-ring" style="left:554px;top:2039px" aria-label="FriendSpace"></div>
  <div class="social-ring" style="left:606px;top:2039px" aria-label="SnapGallery"></div>
</section>

<!-- Blog -->
<section>
  <h2 class="heading abs center" style="left:0;width:1200px;top:2210px;font-size:31px">Latest Blogs</h2>
  <div class="section-rule" style="top:2251px"></div>
  <p class="abs center" style="left:340px;width:520px;top:2270px;font-size:14.5px;line-height:26px;color:#444">Lorem ipsum dolor sit amet, consectetur adipiscing elit, sed do eiusmod tempor incididunt ut labore et dolore magna aliqua.</p>

  <div class="photo" style="left:123px;top:2355px;width:462px;height:316px;border-radius:0;background:linear-gradient(180deg,#e9a23a 0%,#d4782a 55%,#3a2a1c 100%)" role="img" aria-label="Silhouette at sunset over the sea"></div>
  <article class="abs" style="left:156px;top:2535px;width:464px;height:199px;background:var(--white);box-shadow:0 0 10px rgba(0,0,0,.1);padding:28px 26px">
    <div class="blog-meta">&#9719; February 28,2022</div>
    <h3 class="blog-title" style="margin-top:10px">Sed ut perspiciatis unde omnis iste</h3>
    <p class="blog-ex" style="margin-top:8px;width:350px">Lorem ipsum dolor sit amet, consectetur adipiscing elit, sed do eiusmod tempor incididunt ut labore et dolore magna</p>
    <p class="read" style="margin-top:14px">READ MORE &rarr;</p>
    <div class="abs" style="left:407px;top:62px;width:34px;height:32px;background:var(--aqua-dark);color:#fff;display:flex;align-items:center;justify-content:center">&rsaquo;</div>
    <div class="abs" style="left:407px;top:104px;width:34px;height:32px;background:#b5b5b5;color:#fff;display:flex;align-items:center;justify-content:center">&lsaquo;</div>
  </article>

  <div class="photo" style="left:644px;top:2351px;width:190px;height:178px;border-radius:0;background:linear-gradient(180deg,#e2a24a 0%,#c58451 50%,#6d7680 100%)" role="img" aria-label="Person meditating on a beach at sunset"></div>
  <article class="abs" style="left:860px;top:2350px;width:220px">
    <div class="blog-meta">&#9719; February 28,2022</div>
    <h3 class="blog-title" style="margin-top:8px">Sed ut perspiciatis unde omnis iste</h3>
    <p class="blog-ex" style="margin-top:10px">Lorem ipsum dolor sit amet, consectetur adipiscing elit, sed do eiusmod tempor incididunt</p>
    <p class="read" style="margin-top:10px">READ MORE &rarr;</p>
  </article>

  <div class="photo" style="left:644px;top:2556px;width:190px;height:178px;border-radius:0;background:linear-gradient(180deg,#8fb7d6 0%,#7f9a6a 45%,#5a7b44 100%)" role="img" aria-label="Trail runner on a mountain path"></div>
  <article class="abs" style="left:860px;top:2554px;width:220px">
    <div class="blog-meta">&#9719; February 28,2022</div>
    <h3 class="blog-title" style="margin-top:8px">Sed ut perspiciatis unde omnis iste</h3>
    <p class="blog-ex" style="margin-top:10px">Lorem ipsum dolor sit amet, consectetur adipiscing elit, sed do eiusmod tempor incididunt</p>
    <p class="read" style="margin-top:10px">READ MORE &rarr;</p>
  </article>
</section>

<!-- Certification -->
<section>
  <div class="band" style="top:3049px;height:589px"></div>
  <div class="photo" style="left:182px;top:2827px;width:836px;height:471px;background:linear-gradient(180deg,#1d4f7a 0%,#2b6394 50%,#173f66 100%)" role="img" aria-label="Adult and child surfing together on the ocean"></div>
  <svg class="chev" style="left:70px;top:3332px" width="20" height="34"><path d="M17 3 4 17l13 14" fill="none" stroke="#111" stroke-width="3.5"/></svg>
  <svg class="chev" style="left:1105px;top:3332px" width="20" height="34"><path d="m3 3 13 14L3 31" fill="none" stroke="#111" stroke-width="3.5"/></svg>
  <h2 class="heading abs center" style="left:0;width:1200px;top:3344px;font-size:31px">Health Coaching Certification</h2>
  <p class="band-text" style="top:3400px">Lorem ipsum dolor sit amet, consectetur adipiscing elit, sed do eiusmod tempor incididunt ut labore et dolore magna aliqua. Ut enim ad minim veniam, quis nostrud exercitation ullamco laboris nisi ut aliquip ex ea commodo consequat. Duis aute irure dolor in reprehenderit in voluptate velit esse cillum dolore eu fugiat nulla pariatur. Excepteur sint occaecat cupidatat non proident, sunt in culpa qui officia deserunt mollit anim id est laborum.</p>
  <a class="btn" style="left:535px;top:3531px;width:128px;height:40px">Read More</a>
</section>

<!-- Practice -->
<section>
  <h2 class="heading abs center" style="left:0;width:1200px;top:3716px;font-size:31px">Health Coaching Practice</h2>
  <div class="practice" style="left:87px"><div class="ring"><i><svg width="44" height="44" viewBox="0 0 44 44" fill="none" stroke="#fff" stroke-width="2"><path d="M16 28a10 10 0 1 1 12 0v4H16z"/><path d="M17 36h10M19 40h6M22 2v4M6 18H2M42 18h-4M9 7l3 3M35 7l-3 3"/></svg></i></div><span>Creativity</span></div>
  <div class="practice" style="left:302px"><div class="ring"><i><svg width="44" height="44" viewBox="0 0 44 44" fill="none" stroke="#fff" stroke-width="2"><path d="M2 18 10 10l8 4 6-4 8 2 10 8-10 10-8 4-6-6-8-2z"/><path d="m18 14 8 8M14 26l6 6M20 22l6 6"/></svg></i></div><span>Relationships</span></div>
  <div class="practice" style="left:517px"><div class="ring"><i><svg width="44" height="44" viewBox="0 0 44 44" fill="none" stroke="#fff" stroke-width="2"><rect x="6" y="16" width="14" height="22"/><rect x="24" y="10" width="14" height="28"/><circle cx="13" cy="9" r="4"/><path d="M28 18h6M28 24h6M10 24h6"/></svg></i></div><span>Movement</span></div>
  <div class="practice" style="left:731px"><div class="ring"><i><svg width="44" height="44" viewBox="0 0 44 44" fill="none" stroke="#fff" stroke-width="2"><circle cx="22" cy="10" r="4"/><path d="M10 6l8 12h8l8-12M18 18v20M26 18v20M6 14l4 4M38 14l-4 4"/></svg></i></div><span>Joy</span></div>
  <div class="practice" style="left:945px"><div class="ring"><i><svg width="44" height="44" viewBox="0 0 44 44" fill="none" stroke="#fff" stroke-width="2"><circle cx="24" cy="14" r="9"/><path d="M24 9v10M21 12h5M21 16h5M2 32h10l8 4h10l10-8-4-2-8 4H20"/></svg></i></div><span>Finances</span></div>
</section>

<!-- Footer -->
<footer class="footer">
  <div class="logo" style="left:110px;top:118px">colettemarsh</div>
  <h4 style="left:379px">QUICK LINKS</h4>
  <ul style="left:379px;top:140px"><li>Home</li><li>Services</li><li>Coaching Philosophy</li><li>About Me</li></ul>
  <h4 style="left:571px">CONTACT US</h4>
  <div class="contact-row" style="top:148px">
    <svg width="14" height="20" viewBox="0 0 14 20"><path d="M7 19S1 11 1 7a6 6 0 0 1 12 0c0 4-6 12-6 12z" fill="#fff"/><circle cx="7" cy="7" r="2.2" fill="var(--footer)"/></svg>
    <span>Colette Marsh, PhD, LLC<br>© 2022</span>
  </div>
  <div class="contact-row" style="top:212px">
    <svg width="16" height="16" viewBox="0 0 16 16"><path d="M3 1l3 3-2 2c1 2 4 5 6 6l2-2 3 3-2 2C7 15 1 9 1 3z" fill="#fff"/></svg>
    <span>555-314-2786</span>
  </div>
  <div class="contact-row" style="top:248px">
    <svg width="16" height="14" viewBox="0 0 16 14"><rect x="0" y="1" width="16" height="12" rx="1" fill="#fff"/><path d="m1 2 7 6 7-6" fill="none" stroke="var(--footer)" stroke-width="1.5"/></svg>
    <span>colette@colettemarshwell.com</span>
  </div>
  <h4 style="left:863px">NEWSLETTER</h4>
  <div class="abs" style="left:863px;top:144px;width:226px;height:40px;background:#fff;border-radius:3px;display:flex;align-items:center;padding-left:14px;color:#777;font-size:14px">Enter email</div>
  <div class="abs" style="left:1035px;top:144px;width:54px;height:40px;background:var(--green);border-radius:0 3px 3px 0;display:flex;align-items:center;justify-content:center">
    <svg width="16" height="12"><rect width="16" height="12" rx="1" fill="#fff"/><path d="m1 1 7 6 7-6" fill="none" stroke="var(--green)" stroke-width="1.5"/></svg>
  </div>
  <div class="abs" style="left:872px;top:223px;display:flex;gap:4px" aria-label="Accepted payment methods">
    <i class="pay" style="background:#3a3a3a"></i><i class="pay" style="background:#e6e6e6"></i><i class="pay" style="background:#f2f2f2"></i><i class="pay" style="background:#dcdcdc"></i><i class="pay" style="background:#2d6fb5"></i><i class="pay" style="background:#ececec"></i>
  </div>
  <p class="abs center" style="left:0;width:1200px;top:330px;font-size:14px">©Copyrights 2022 Colette Marsh &nbsp;| &nbsp; All Rights Reserved</p>
  <div class="abs" style="left:1044px;top:300px;width:42px;height:42px;border-radius:50%;background:var(--aqua-dark);display:flex;align-items:center;justify-content:center">
    <svg width="18" height="16"><path d="M9 1C4.5 1 1 3.8 1 7.2c0 1.8 1 3.4 2.6 4.5L3 15l3.6-2C7.4 13.2 8.2 13.4 9 13.4c4.5 0 8-2.8 8-6.2S13.5 1 9 1z" fill="#fff"/></svg>
  </div>
</footer>
<div class="foot-social" style="left:112px" aria-label="FriendSpace"></div>
<div class="foot-social" style="left:168px" aria-label="ChirpLine"></div>
<div class="foot-social" style="left:221px" aria-label="SnapGallery"></div>
<div class="foot-social" style="left:277px" aria-label="ConnectWork"></div>

</body>
</html>
```